Tallow Farm Brochure

To design a small brochure that tells people about our U-Pick cherry farm, where we are, when we are open and what our contact details are.

We have existing logo's which should be used. I have uploaded a file with these details.

Details about us are all located on:-
www.friendlink.example/tallowfarm
https://circlepage.example/u/0/b/704916382057419263851/704916382057419263851/about/p/pub

Farm

```html
<!DOCTYPE html>
<html lang="en">
<head>
<meta charset="utf-8">
<title>Tallow Farm Brochure</title>
<link rel="stylesheet" href="https://fonts.googleapis.com/css2?family=Roboto+Condensed:wght@400;700&family=Great+Vibes&family=Crimson+Text:wght@400&display=swap">
<style>
  :root {
    --teal: #1a9c8a;
    --teal-dark: #0f7f70;
    --lime: #8cc63f;
    --green-text: #2e9b57;
    --cherry: #c8102e;
    --cherry-dark: #7a0010;
    --pink: #f06ea9;
    --ink: #4a4a4a;
    --paper: #ffffff;
    --panel-glass: rgba(255,255,255,0.55);
  }
  * { margin: 0; padding: 0; box-sizing: border-box; }
  html, body { width: 849px; height: 1200px; overflow: hidden; background: var(--paper); }
  .brochure { position: relative; width: 849px; height: 1200px; overflow: hidden; background: var(--paper);
    font-family: "Roboto Condensed", "Arial Narrow", sans-serif; }

  .orchard-photo { position: absolute; left: 13px; top: 13px; width: 509px; height: 255px;
    background: linear-gradient(180deg, #bcd9ef 0%, #dfeef5 22%, #6f9a4a 34%, #7fb347 60%, #5f8f33 100%); }

  .logo-panel { position: absolute; left: 537px; top: 13px; width: 273px; height: 255px; }
  .logo-panel svg { position: absolute; inset: 0; }
  .logo-name { position: absolute; left: 0; right: 16px; top: 52px; text-align: center;
    font-weight: 700; font-size: 60px; line-height: 0.95; color: var(--green-text); }
  .logo-name span { display: block; font-size: 44px; }
  .logo-url { position: absolute; left: 0; right: 16px; top: 163px; text-align: center;
    font-size: 10px; font-weight: 700; color: var(--green-text); }

  .story-panel { position: absolute; left: 13px; top: 283px; width: 797px; height: 635px;
    background: linear-gradient(180deg, #c9dcc0 0%, #b7d0a8 40%, #cfe0c6 70%, #dfe9d6 100%); }
  .story-panel svg.bands { position: absolute; inset: 0; }
  .cherry-photo { position: absolute; left: 212px; top: 22px; width: 386px; height: 248px; border-radius: 50%;
    border: 6px solid #fff; box-shadow: 0 2px 10px rgba(0,0,0,0.35);
    background: radial-gradient(ellipse at 55% 45%, #e3303f 0%, var(--cherry) 45%, var(--cherry-dark) 100%); }

  .story-title { position: absolute; left: 50px; top: 255px; font-family: "Great Vibes", cursive;
    font-size: 58px; font-weight: 400; color: var(--cherry); line-height: 1; }
  .story-text { position: absolute; left: 32px; top: 307px; width: 731px; height: 322px;
    background: var(--panel-glass); padding: 10px 14px; color: var(--ink); font-size: 9.3px; line-height: 1.45; }
  .story-text p { margin-bottom: 9px; }
  .story-text .lead-name { font-weight: 700; font-size: 15px; color: var(--teal-dark); }

  .quote { position: absolute; left: 0; right: 0; top: 932px; text-align: center;
    font-family: "Crimson Text", serif; font-size: 17px; color: #333; }

  .footer-shapes { position: absolute; left: 0; top: 0; }
  .contact-card { position: absolute; left: 30px; top: 972px; width: 310px; height: 178px; border-radius: 22px;
    background: var(--pink); color: #fff; padding: 14px 8px 0 20px; font-size: 13px; line-height: 1.45;
    letter-spacing: -0.1px; white-space: nowrap; overflow: hidden; }
  .contact-card .phone { font-size: 28px; line-height: 1; margin-top: 10px; letter-spacing: 0.5px; }

  .van-photo { position: absolute; left: 388px; top: 970px; width: 408px; height: 140px; border-radius: 30px 40px 16px 16px;
    background: linear-gradient(180deg, #f4f6f5 0%, #e3e7e5 70%, #9aa3a0 100%); }
</style>
</head>
<body>
<main class="brochure">
  <div class="orchard-photo" role="img" aria-label="Photo of young cherry trees in rows on green grass with hills behind"></div>

  <div class="logo-panel">
    <svg width="273" height="255" viewBox="0 0 273 255">
      <path d="M0 255 C120 240 230 180 273 30 L273 255 Z" fill="var(--teal)"/>
      <path d="M0 248 C120 232 220 175 262 40 C245 170 150 232 0 255 Z" fill="var(--lime)"/>
    </svg>
    <div class="logo-name">Tallow<span>Farm</span></div>
    <div class="logo-url">www.tallowfarm.example</div>
  </div>

  <section class="story-panel">
    <svg class="bands" width="797" height="635" viewBox="0 0 797 635">
      <path d="M0 60 C80 55 160 70 230 95 L230 110 C160 85 80 72 0 75 Z" fill="var(--teal)"/>
      <path d="M0 75 C80 72 160 85 230 110 L228 118 C160 95 80 84 0 88 Z" fill="var(--lime)"/>
      <path d="M590 175 C660 180 730 168 797 130 L797 205 C730 230 660 225 590 215 Z" fill="var(--teal)"/>
      <path d="M590 215 C660 225 730 230 797 205 L797 218 C730 240 660 236 590 226 Z" fill="var(--lime)"/>
    </svg>
    <div class="cherry-photo" role="img" aria-label="Close-up photo of ripe red cherries with water droplets"></div>
    <h2 class="story-title">Story</h2>
    <div class="story-text">
      <p><span class="lead-name">Tallow Farm</span> is in the beautiful Lindell Valley, an ideal location for growing sweet juicy cherries. Visit us for Pick Your Own or Pre-Picked Cherries.</p>
      <p>When picking, you can eat as much as you want. Prices for take away U-Pick fruit is $8 per kilo. There are no entry fees.</p>
      <p>Visitors are welcome to picnic beside our scenic dam and enjoy the views of the valley, the neighboring vineyards and the distant mountain ranges.</p>
      <p>When you first arrive at our farm we can show you how to pick cherries and where the best cherries are on that day. Farmer Tom can also show you around the farm and explain how the cherries are grown and the organic principles we employ in managing our trees.</p>
      <p>Cherries have been grown at Tallow Farm for the last 50 or so years. Some of our trees today date back to these original plantings.</p>
      <p>Our cherry trees are pruned to enable easy picking for people of all ages. We have over 4,000 trees which ensures we always have more than plenty of juicy ripe fruit to pick.</p>
      <p>We have 12 varieties of cherries, most of which are heritage varieties and are rarely found elsewhere. Some have dark, near black fruit, some have bright mahogany sweet highly juicy fruit and others have red firm fruit. Our cherries are known as mid-season cherries and are typically available in November and December, sometimes still available at the beginning of January.</p>
      <p>Tallow Farm was previously run by two successive generations of the Harlow Family, the most recent Harlow Family member owner being the Vice President of the Regional Cherry Growers Guild. Farmer Tom bought Tallow Farm from the Harlow family in early 2014.</p>
      <p>Farmer Tom is a third generation farmer, his grandfather having first farmed in the lowlands in Scotland on a mixed farm. When one of the daughters of his grandfather married (Tom's mum), she moved to South Australia and together with Tom's dad, they grew Almonds in the Marrow Creek Region. Farmer Tom worked on the Almond farm for many years, eventually moving to Victoria where he commenced Cherry farming by buying Tallow Farm.</p>
    </div>
  </section>

  <p class="quote">"It's the magnificent views and our happy trees. That's what makes our cherries juicier and sweeter." Farmer Tom.</p>

  <svg class="footer-shapes" width="849" height="1200" viewBox="0 0 849 1200">
    <path d="M0 925 L0 1200 L90 1200 C60 1120 40 1010 0 925 Z" fill="var(--teal)"/>
    <path d="M0 918 C30 960 50 1000 60 1040 C40 1000 20 965 0 940 Z" fill="var(--lime)"/>
    <path d="M330 1200 C500 1170 700 1150 849 1090 L849 1200 Z" fill="var(--teal)"/>
    <path d="M300 1200 C480 1165 690 1140 849 1080 L849 1090 C700 1150 500 1170 330 1200 Z" fill="var(--lime)"/>
  </svg>

  <div class="contact-card">
    Tallow Farm is in the beautiful Lindell Valley,<br>
    an ideal location for growing sweet juicy cherries.<br>
    Visit us for Pick Your Own or Pre-Picked Cherries.<br>
    14 Orchard Ridge Road Tallow, Victoria<br>
    Fri - Sun: 10:00 am - 5:00 pm
    <div class="phone">+61 1300 555 017</div>
  </div>

  <div class="van-photo" role="img" aria-label="Photo of a white delivery van with green farm livery and phone number 555-010-246"></div>
</main>
</body>
</html>
```